Web-Design for Electrcian Company

Our Customer is a small business electrian in Switzerland. He is looking for a fresh and innovative website design. He is well known for his extra service, and that they always go for the extra-mile! In his logo you also see that positive and fresh image the try to bring to the customer. the main colors are black, red and white.

the website structure will be:

- home
- services (with submenu for each service)
- references (with submenu for each category of services)
- about us (2 submenus: history and staff)
- links
- Contact

Reason: We are discussing the Proposals with the customer right now

Target Market(s)

Architects, building owners, people from the age of 35 up...

Industry/Entity Type

Small Business

```html
<!DOCTYPE html>
<html lang="en">
<head>
<meta charset="utf-8">
<title>Brunner + Meier Elektro AG</title>
<link rel="stylesheet" href="https://fonts.googleapis.com/css2?family=Arimo:wght@400;700&family=Fira+Sans+Condensed:wght@500&family=Open+Sans:wght@700&display=swap">
<style>
:root{
  --red:#d7232a;
  --ink:#1a1a1a;
  --text:#2b2b2b;
  --muted:#444;
  --band-top:#e9e9e9;
  --band-bottom:#d9d9d9;
  --white:#fff;
  --yellow-dark:#c49a00;
  --yellow-light:#ffe600;
}
*{margin:0;padding:0;box-sizing:border-box}
html,body{width:1200px;height:1200px;overflow:hidden;background:var(--white)}
body{position:relative;font-family:"Arimo",Arial,sans-serif;color:var(--text)}
.top-band{position:absolute;left:0;top:0;width:1200px;height:500px;
  background:linear-gradient(180deg,var(--band-top) 0%,#f1f1f1 40%,var(--band-bottom) 100%);
  border-top:3px solid #333}
.brand-name{position:absolute;white-space:nowrap;font-family:"Arimo",Arial,sans-serif;font-weight:700;color:var(--ink)}
.brand-header{left:130px;top:58px;font-size:17px;line-height:20px}
.brand-footer{right:130px;top:898px;font-size:14px;line-height:18px}
.main-nav{position:absolute;top:60px;left:565px;display:flex;font-family:"Open Sans",sans-serif;font-weight:700;font-size:12px;color:var(--ink)}
.main-nav a{color:inherit;text-decoration:none;display:flex;align-items:center;gap:8px}
.main-nav .active{color:var(--red)}
.hero{position:absolute;left:130px;top:130px;width:940px;height:240px;border:1px solid #fff;box-shadow:0 0 4px rgba(0,0,0,.25);display:flex}
.hero-copy{position:relative;width:440px;height:100%;background:linear-gradient(100deg,var(--yellow-dark) 0%,#e9be00 55%,var(--yellow-light) 100%);padding:24px 29px}
.hero-title{font-family:"Fira Sans Condensed",sans-serif;font-weight:500;font-size:23px;line-height:28px;color:var(--ink);margin-bottom:6px}
.hero-copy p{font-size:12px;line-height:15px;color:var(--ink);margin-bottom:6px}
.learn-more{position:absolute;left:29px;top:132px;display:flex;align-items:center;gap:9px;font-weight:700;font-size:12px;color:var(--ink)}
.slider{position:absolute;left:129px;top:192px}
.hero-photo{flex:1;background:linear-gradient(100deg,#4a4038 0%,#7a6a55 30%,#3e3a35 55%,#c99a2a 75%,#5a4634 100%)}
.features{position:absolute;top:408px;left:130px;display:flex}
.feature{width:240px;display:flex;gap:28px}
.feature svg{flex:none;margin-top:2px}
.feature h3{font-size:14px;font-weight:700;color:#3a3a3a;line-height:15px}
.feature p{font-size:12px;line-height:15px;color:var(--muted)}
.col{position:absolute;top:518px;width:300px;font-size:12px;line-height:14.5px;color:var(--text)}
.col h2{font-size:14px;font-weight:700;color:var(--red);margin-bottom:17px}
.col p{margin-bottom:14px}
.indent{text-indent:36px}
.col-about{left:130px}
.col-cases{left:450px}
.team-photo{position:absolute;left:769px;top:519px;width:302px;height:122px;background:var(--white);border:1px solid #ccc;padding:3px;box-shadow:0 6px 6px -4px rgba(0,0,0,.45)}
.team-photo div{width:100%;height:100%;background:linear-gradient(180deg,#3b4356 0%,#2c3140 55%,#8a8a88 100%)}
.address{position:absolute;left:770px;top:658px;font-size:12px;line-height:14px;font-style:normal;color:var(--text)}
.address strong{display:block;margin-top:14px}
.footer-rule{position:absolute;left:130px;top:859px;width:940px;height:6px;border-top:2px solid #222;border-bottom:1px solid #222}
.legal{position:absolute;left:130px;top:883px;font-size:11px;line-height:14px;color:var(--text)}
.legal nav{margin-top:6px}
.legal nav span{margin:0 6px}
</style>
</head>
<body>
<div class="top-band"></div>

<header>
  <div class="brand-name brand-header">Brunner + Meier Elektro AG</div>
  <nav class="main-nav">
    <a class="active" href="#" style="margin-right:37px">HOME</a>
    <a href="#" style="margin-right:20px">SERVICES <svg width="8" height="6"><path d="M1 1l3 3 3-3" fill="none" stroke="#1a1a1a" stroke-width="1.3"/></svg></a>
    <a href="#" style="margin-right:20px">REFERENCES <svg width="8" height="6"><path d="M1 1l3 3 3-3" fill="none" stroke="#1a1a1a" stroke-width="1.3"/></svg></a>
    <a href="#" style="margin-right:20px">ABOUT US <svg width="8" height="6"><path d="M1 1l3 3 3-3" fill="none" stroke="#1a1a1a" stroke-width="1.3"/></svg></a>
    <a href="#" style="margin-right:38px">LINKS</a>
    <a href="#">CONTACT</a>
  </nav>
</header>

<section class="hero">
  <div class="hero-copy">
    <h1 class="hero-title">Electrical Service Solutions</h1>
    <p>Lorem ipsum dolor sit amet, consectetur adipiscing elit. Sed consequat consectetur dignissim. Sed ac libero sapien.</p>
    <p>Mauris semper ullamcorper dolor, id aliquam risus semper in.</p>
    <div class="learn-more">Learn More
      <svg width="20" height="20" viewBox="0 0 20 20"><circle cx="10" cy="10" r="8.5" fill="none" stroke="#1a1a1a" stroke-width="1.6"/><path d="M5.5 10h8M10 6.5l3.5 3.5-3.5 3.5" fill="none" stroke="#1a1a1a" stroke-width="1.8"/></svg>
    </div>
    <svg class="slider" width="182" height="30" viewBox="0 0 182 30">
      <g stroke="#fff" stroke-width="1.5" fill="none">
        <path d="M0 22h58"/><circle cx="62" cy="22" r="4"/><path d="M62 18v-4M62 2v10M56 7h12"/>
        <circle cx="116" cy="22" r="4"/><path d="M120 22h61M110 6h12"/>
      </g>
    </svg>
  </div>
  <div class="hero-photo" role="img" aria-label="Electrician in a yellow hard hat working on a network cabinet full of colourful cables"></div>
</section>

<section class="features">
  <div class="feature">
    <svg width="32" height="28" viewBox="0 0 32 28"><rect x="1" y="1" width="30" height="26" rx="2" fill="#222"/><text x="16" y="21" font-family="Arimo,sans-serif" font-weight="700" font-size="18" fill="#fff" text-anchor="middle">$¢</text></svg>
    <div><h3>Save big with us</h3><p>Lorem ipsum dolor sit amet, consectetur adipiscing elit.</p></div>
  </div>
  <div class="feature">
    <svg width="32" height="32" viewBox="0 0 32 32"><circle cx="16" cy="16" r="15" fill="#222"/><path d="M16 6v10l6 6" stroke="#fff" stroke-width="2" fill="none"/></svg>
    <div><h3>24 Hour Service</h3><p>Lorem ipsum dolor sit amet, consectetur adipiscing elit.</p></div>
  </div>
  <div class="feature">
    <svg width="32" height="32" viewBox="0 0 32 32"><path d="M16 2a3 3 0 0 1 2 1c5 1 7 6 7 12v6l4 4H3l4-4v-6c0-6 2-11 7-12a3 3 0 0 1 2-1z" fill="#222"/><circle cx="16" cy="28" r="3" fill="#222"/></svg>
    <div><h3>Door-Bell Systems</h3><p>Lorem ipsum dolor sit amet, consectetur adipiscing elit.</p></div>
  </div>
  <div class="feature">
    <svg width="32" height="32" viewBox="0 0 32 32" fill="#222"><rect x="0" y="0" width="14" height="14" rx="1.5"/><rect x="18" y="0" width="14" height="14" rx="1.5"/><rect x="0" y="18" width="14" height="14" rx="1.5"/><rect x="18" y="18" width="14" height="14" rx="1.5"/></svg>
    <div><h3>Fuse Panels</h3><p>Lorem ipsum dolor sit amet, consectetur adipiscing elit.</p></div>
  </div>
</section>

<section class="col col-about">
  <h2>Brunner+Meier Elektro AG</h2>
  <p class="indent">Lorem ipsum dolor sit amet, consectetur adipiscing elit. Sed consequat consectetur dignissim. Sed ac libero sapien.</p>
  <p>Mauris semper ullamcorper dolor, id aliquam risus semper in. Suspendisse potenti. Quisque et dui tellus. Integer fringilla ante nec risus eleifend dignissim.</p>
  <p>Donec metus elit, varius sit amet scelerisque at, malesuada vel metus.</p>
</section>

<section class="col col-cases">
  <h2>Case Studies</h2>
  <p>- Lorem ipsum dolor sit amet, consectetur adipiscing elit. Sed consequat consectetur dignissim. Sed ac libero sapien.</p>
  <p>- Mauris semper ullamcorper dolor, id aliquam risus semper in. Suspendisse potenti. Quisque et dui tellus. Integer fringilla ante nec risus eleifend dignissim.</p>
  <p>- Donec metus elit, varius sit amet scelerisque at, malesuada vel metus.</p>
</section>

<figure class="team-photo"><div role="img" aria-label="Team photo of staff in white shirts standing between company cars, seen from above"></div></figure>

<address class="address">
  Brunner + Meier Elektro AG<br>Lindenweg 12<br>Postfach 318<br>9200 Gossau
  <strong>Tel 071/456 21 30</strong>
  <strong>Fax 071/456 21 31</strong>
</address>

<div class="footer-rule"></div>
<footer class="legal">
  <p>Copyright © 2012 Brunner+Meier Elektro AG. All rights reserved.</p>
  <nav>Disclaimer<span>|</span>Sitemap<span>|</span> Privacy Policy</nav>
</footer>
<div class="brand-name brand-footer">Brunner + Meier Elektro AG</div>
</body>
</html>
```